Technology Company Web Design Project

We are working with BrimLoop. They are a technology company and in need of a new website design.
BrimLoop helps companies control who (or what) can access which information inside their systems — and under what conditions. Think of them as the traffic controller for digital access and data permissions.
Instead of letting every app, employee, or AI bot freely connect to everything, GateMarrow makes sure:
• Each one only gets access to what it actually needs.
• That access follows company rules automatically.
• Those rules are enforced the same way everywhere — across apps, servers, and even AI tools.
Some competitor sites to use for inspiration:
https://www.korvanshield.com/en/lp/ac/korvanmesh.html
https://www.dunmerecharter.org
https://www.qelvo.com
Thank you for taking the time to consider designing a website for us. We are web developers based in Stockton and Los Angeles, CA, USA. Most of our projects go through the same process. Understanding this process may help you win a project with us. We custom-code all of our websites in-house. We don’t have any requirements as to what tools you use for your design, but we prefer Figma files. For any design that we label as four-stars, we send it to the client for review. The client picks the final design they want us to use. Once we complete this process, we will continue to show additional clients all the four-star sites and purchase them later. Your designs will have multiple chances to sell. For better chances of success, we ask that you follow these guidelines.
IMAGES:
If you use any images or icons in the design, we ask that you have a link to the asset so we can purchase the image/icon. Most of the designs we submit do not have the customer’s images on them unless they have some great images. Be creative; show us the feeling you are trying to portray with your image choices. Use any royalty-free site you choose. We subscribe to Tarsel and mainly use their images, but we can purchase images outside of Tarsel.
PLEASE NOTE: we will not submit designs to clients with watermarks on the images.
FONTS:
We ask that you identify the fonts used in the design. This can be done in a message if you want. We typically use Google Fonts and Tarsel Fonts.
CONTENT:
We're always open to different content and ideas. We often submit designs with stock images so the client can see our vision. We typically take pictures after the website launch to use their images with our vision. Lorem Ipsum is fine for paragraphs, but we ask that you write the headers in correct English. We want to be able to show the vision and identify the sections of the website.
INSPIRATION:
We typically add a couple of links in the brief of websites we like to help you get started in your design.
REVISIONS:
We do not often ask for revisions of the designs unless we see something in the design that may not appeal to the client. If there are slight changes that we want to make, we do that in the development process.
FEEDBACK:
We rarely give feedback on designs during the design process. We are working on many website projects and do not have the time to provide feedback. We usually respond if your request is well thought out and asks specific questions, but a note asking “feedback, please” usually goes unanswered.

```html
<!DOCTYPE html>
<html lang="en">
<head>
<meta charset="utf-8">
<title>BrimLoop — Control Access. Everywhere. Instantly.</title>
<link href="https://fonts.googleapis.com/css2?family=Inter:wght@300;400;500;600;700&display=swap" rel="stylesheet">
<style>
:root{
  --orange:#e8792d;
  --orange-soft:#fdf1e8;
  --navy:#1d2c47;
  --ink:#1e2533;
  --text:#4a4f59;
  --muted:#8a8f98;
  --line:#e3e5e8;
  --gray-bg:#f4f4f5;
  --white:#ffffff;
}
*{box-sizing:border-box;margin:0;padding:0}
html,body{width:1200px;height:5112px;overflow:hidden;background:var(--white)}
body{font-family:'Inter',sans-serif;color:var(--ink);position:relative}
section,footer,header{position:relative;width:1200px}
.abs{position:absolute}
.brand{display:flex;align-items:center;gap:8px;font-weight:700;font-size:17px;color:var(--orange);letter-spacing:.5px}
.brand .dot{width:14px;height:14px;border-radius:50%;background:var(--navy)}

/* hero */
.hero{height:744px}
.nav a{position:absolute;top:29px;font-size:12.5px;color:#3a3f48;text-decoration:none}
.hero h1{left:86px;top:182px;font-size:58px;line-height:74px;font-weight:400;color:var(--ink);letter-spacing:-.5px}
.hero .lead{left:86px;top:414px;width:440px;font-size:13.5px;line-height:23px;color:var(--text)}
.btn{position:absolute;height:42px;border-radius:6px;font-size:12.5px;display:flex;align-items:center;justify-content:center}
.btn-primary{background:var(--orange);color:#fff}
.btn-outline{border:1.5px solid #f0c7a8;color:var(--orange);background:#fff}
.trusted{left:86px;top:622px;width:200px;font-size:12px;line-height:18px;color:var(--muted)}
.logo-row{display:flex;align-items:center;justify-content:space-between}
.logo-item{display:flex;align-items:center;gap:7px;font-size:17px;font-weight:600;color:#9aa0a8}
.logo-item .mk{width:14px;height:14px;border-radius:50%;background:#b9bec5}
.node{position:absolute;background:#fff;border:1.5px solid var(--line);border-radius:6px;padding:10px 12px}
.node h4{font-size:11.5px;font-weight:500;color:var(--ink)}
.node p{font-size:10.5px;color:var(--muted);margin-top:12px}
.node.active{border:2px solid #f3a56e;box-shadow:0 0 0 4px #fde7d6}
.code-box{left:674px;top:432px;width:246px;height:84px;border:2px solid #d6d8dc;border-radius:6px;padding:10px 12px;background:#fff}
.digits{display:flex;gap:10px}
.digits span{width:28px;height:30px;border:1px solid var(--line);border-radius:4px;display:flex;align-items:center;justify-content:center;font-size:14px;color:var(--ink)}
.code-box p{font-size:10.5px;color:var(--muted);margin-top:10px}

/* intro band */
.intro{height:934px;background:var(--gray-bg)}
.statement{left:106px;top:84px;width:1010px;font-size:38.5px;line-height:53px;font-weight:400;color:var(--ink);letter-spacing:-.3px}
.intro h2{left:106px;top:368px;font-size:31px;font-weight:400;color:var(--ink)}
.dash{left:105px;top:476px;width:990px;height:350px;background:#fff;border-radius:6px;overflow:hidden;box-shadow:0 1px 3px rgba(0,0,0,.05)}
.dash .side{left:0;top:0;width:190px;height:100%;border-right:1px solid var(--line);padding:16px 12px}
.side .brand{justify-content:center;font-size:13px;margin:6px 0 18px}
.side .search{height:22px;border:1px solid var(--line);border-radius:4px;font-size:9px;color:var(--muted);padding:5px 8px}
.side ul{list-style:none;margin-top:10px}
.side li{font-size:9px;color:#666;padding:6px 8px;display:flex;gap:6px;align-items:center}
.side li i{width:8px;height:8px;border-radius:2px;border:1px solid #aaa;display:inline-block}
.side .folder i{background:#f2b27f;border:none}
.side .label{font-size:8.5px;color:var(--muted);padding:8px 8px 2px}
.dash .topbar{left:190px;top:0;right:0;height:32px;border-bottom:1px solid var(--line);font-size:11px;font-weight:500;padding:10px 14px}
.topbar .share{position:absolute;right:40px;top:7px;border:1px solid var(--line);border-radius:4px;font-size:8.5px;padding:3px 8px;font-weight:400}
.topbar .avatar{position:absolute;right:12px;top:6px;width:18px;height:18px;border-radius:50%;background:#c9bfb3}
.dash .listhead{left:204px;top:52px;font-size:13px;font-weight:500}
.dash .listsub{left:204px;top:70px;font-size:8.5px;color:var(--muted)}
.dash .tools{right:14px;top:54px;display:flex;gap:8px}
.tools span{height:20px;border:1px solid var(--line);border-radius:4px;font-size:8.5px;color:#666;padding:4px 8px}
.intcard{position:absolute;width:252px;height:132px;border:1px solid var(--line);border-radius:6px;padding:12px}
.intcard .ic{width:22px;height:22px;border-radius:5px}
.intcard .url{position:absolute;right:12px;top:12px;font-size:8px;color:var(--muted);text-decoration:underline}
.intcard h5{font-size:11px;font-weight:500;margin-top:14px}
.intcard p{font-size:8px;line-height:12px;color:var(--muted);margin-top:4px}
.intcard .foot{position:absolute;left:12px;right:12px;bottom:10px;border-top:1px solid var(--line);padding-top:8px;font-size:8px;color:#666}
.toggle{position:absolute;right:0;top:6px;width:26px;height:14px;border-radius:8px;background:#ddd}
.toggle.on{background:#f3a56e}
.dash .fade{left:0;right:0;bottom:0;height:170px;background:linear-gradient(to bottom,rgba(255,255,255,0),#fff 85%)}

/* why */
.why{height:652px}
.section-title{left:0;width:1200px;text-align:center;font-size:39px;font-weight:400;color:var(--ink);letter-spacing:-.3px}
.feat{position:absolute;width:325px;border:1.5px solid var(--line);border-radius:3px;padding:20px;background:#fff}
.feat .icon{width:46px;height:46px;border-radius:6px;background:var(--orange-soft);border:1px solid #f6d5bd;display:flex;align-items:center;justify-content:center}
.feat .icon b{width:22px;height:22px;border:2px solid var(--orange);border-radius:6px;opacity:.7}
.feat h3{font-size:14px;font-weight:500;margin-top:26px;color:var(--ink)}
.feat p{font-size:12.5px;line-height:20px;color:var(--text);margin-top:4px}
.feat.dark{background:var(--navy);border-color:var(--navy)}
.feat.dark h3,.feat.dark p{color:#fff}
.feat.dark .icon{background:#f6b98c;border:none}
.feat.dark .icon b{border-color:#fff}

/* built */
.built{height:978px}
.panel{position:absolute;border:1.5px solid var(--line);border-radius:3px;background:#fff;overflow:hidden}
.panel h3{font-size:14px;font-weight:500;color:var(--ink)}
.panel .desc{font-size:12.5px;line-height:20px;color:var(--text);margin-top:8px}
.login-back{position:absolute;background:#f6f6f7;border:1px solid #eee;border-radius:4px}
.login{position:absolute;left:143px;top:26px;width:206px;height:258px;background:#fff;border:1px solid var(--line);border-radius:4px;padding:14px 16px;text-align:center}
.login .brand{justify-content:center;font-size:9px;gap:4px}
.login .brand .dot{width:7px;height:7px}
.login h6{font-size:9px;font-weight:500;margin-top:8px}
.login .sm{font-size:6px;color:var(--muted)}
.login .sso{display:flex;gap:6px;margin-top:10px}
.login .sso span{flex:1;height:14px;border:1px solid var(--line);border-radius:3px;font-size:5.5px;line-height:12px}
.login .field{text-align:left;font-size:6px;color:#555;margin-top:8px}
.login .field div{height:14px;border:1px solid var(--line);border-radius:3px;margin-top:3px}
.login .row{display:flex;justify-content:space-between;font-size:5.5px;margin-top:8px;color:#555}
.login .row em{color:var(--orange);font-style:normal}
.login .go{height:14px;background:var(--orange);border-radius:3px;margin-top:8px;font-size:6px;color:#fff;line-height:14px}
.flow{position:absolute;background:#fff;border:1px solid var(--line);border-radius:5px;padding:10px 12px}
.flow h6{font-size:11.5px;font-weight:500}
.flow p{font-size:10.5px;color:var(--muted);margin-top:10px}
.flow.hot{border:2px solid #f3a56e;box-shadow:0 0 0 3px #fde7d6;padding:6px 10px;font-size:11px;font-weight:500}
.learn{position:absolute;border:1.5px solid #f3c8a8;border-radius:5px;font-size:11px;color:var(--orange);padding:6px 10px}

/* testimonials */
.voices{height:876px;background:var(--gray-bg)}
.quote{position:absolute;width:420px}
.quote h3{font-size:19px;line-height:27px;font-weight:400;color:var(--ink)}
.quote p{font-size:13.3px;line-height:27px;color:var(--text);margin-top:22px}
.quote .who{font-size:12.5px;color:var(--ink);margin-top:28px}
.quote .role{font-size:12px;color:var(--text);margin-top:4px}
.dots{left:536px;top:714px;display:flex;gap:8px}
.dots span{width:34px;height:5px;border-radius:3px;background:#d5d7db}
.dots span.on{background:var(--orange)}

/* cta */
.cta-wrap{height:470px}
.cta{left:99px;top:66px;width:1002px;height:357px;background:#1f3556;border-radius:2px;text-align:center;color:#fff}
.cta h2{font-size:40px;font-weight:400;margin-top:70px;letter-spacing:-.3px}
.cta p{font-size:13.5px;line-height:19px;color:#c5cedb;margin-top:18px}
.cta .go{display:inline-block;margin-top:50px;background:var(--orange);border:2px solid #fff;border-radius:7px;padding:11px 20px;font-size:12.5px}

/* footer */
.site-foot{height:458px}
.site-foot .rule{left:99px;top:20px;width:1002px;height:1px;background:var(--line)}
.fcol{position:absolute;top:68px}
.fcol h5{font-size:12.5px;font-weight:500;color:var(--ink)}
.fcol a{display:block;font-size:12.5px;color:var(--text);text-decoration:none;margin-top:17px}
.social{display:flex;gap:8px}
.social span{width:22px;height:22px;border:1px solid var(--line);border-radius:4px;display:flex;align-items:center;justify-content:center}
.social span i{width:8px;height:8px;border-radius:2px;background:#9aa0a8}
.legal a{position:absolute;top:369px;font-size:12.5px;color:var(--text);text-decoration:none}
</style>
</head>
<body>

<header class="hero">
  <div class="abs brand" style="left:88px;top:24px"><span class="dot"></span>BrimLoop</div>
  <nav class="nav">
    <a style="left:698px">How it Works</a>
    <a style="left:813px">Why Us</a>
    <a style="left:894px">Use Cases</a>
    <a style="left:993px">Pricing</a>
    <a style="left:1068px">Contact</a>
  </nav>

  <h1 class="abs">Control Access.<br>Everywhere.<br>Instantly.</h1>
  <p class="abs lead">BrimLoop unifies access control across your apps, APIs, and AI systems ensuring every user, service, and agent only gets the data they truly need.</p>
  <a class="btn btn-primary" style="left:86px;top:520px;width:134px">Request a Demo</a>
  <a class="btn btn-outline" style="left:232px;top:520px;width:140px">See How it Works</a>

  <p class="abs trusted">Trusted by the fastest growing companies</p>
  <div class="abs logo-row" style="left:370px;top:628px;width:745px">
    <span class="logo-item"><span class="mk"></span>Harlow</span>
    <span class="logo-item"><span class="mk"></span>Tablewise</span>
    <span class="logo-item"><span class="mk"></span>Chatterbox</span>
    <span class="logo-item"><span class="mk"></span>Tunefold</span>
    <span class="logo-item"><span class="mk"></span>Postwren</span>
  </div>

  <svg class="abs" style="left:0;top:0" width="1200" height="744">
    <path d="M828 239 V266 M700 266 H955 M700 266 V292 M955 266 V335" stroke="#d6d8dc" stroke-width="1.5" fill="none"/>
    <circle cx="828" cy="239" r="4" fill="#e8792d"/>
  </svg>
  <div class="node active" style="left:734px;top:167px;width:188px;height:72px">
    <h4>Multi-Factor / 2FA Protection</h4><p>Add an extra layer of security.</p>
  </div>
  <div class="node" style="left:622px;top:292px;width:158px;height:60px">
    <h4>User &amp; Session Management</h4><p>Stay in control of your users.</p>
  </div>
  <div class="node" style="left:862px;top:335px;width:184px;height:66px">
    <h4>Federated Identity &amp; SSO</h4><p>Give users one click sign-on.</p>
  </div>
  <div class="abs code-box">
    <div class="digits"><span>7</span><span>4</span><span>2</span><span>9</span><span>1</span><span>5</span></div>
    <p>Code Expiration: 20:00</p>
  </div>
</header>

<section class="intro">
  <p class="abs statement">Instead of embedding rules in every system, BrimLoop centralizes &nbsp;policy logic. Every access request — from a user or an AI agent — is &nbsp;checked through our enforcement engine before reaching sensitive data.</p>
  <h2 class="abs">Policy Control That Follows Your Data</h2>

  <div class="abs dash">
    <div class="abs side">
      <div class="brand"><span class="dot" style="width:9px;height:9px"></span>BrimLoop</div>
      <div class="search">Search</div>
      <ul>
        <li><i></i>Dashboard</li>
        <li><i></i>Calendar</li>
        <li><i></i>Updates</li>
      </ul>
      <div class="label">Folders</div>
      <ul style="margin-top:0">
        <li class="folder"><i></i>Personal</li>
        <li class="folder"><i></i>Freelance</li>
        <li class="folder"><i></i>Pages</li>
      </ul>
    </div>
    <div class="abs topbar">Integration<span class="share">Share workspace</span><span class="avatar"></span></div>
    <div class="abs listhead">Integration list</div>
    <div class="abs listsub">Manage and connect your favourite apps to boost productivity.</div>
    <div class="abs tools"><span style="width:150px">Search</span><span>Grid</span><span>List</span></div>

    <div class="intcard" style="left:204px;top:98px">
      <div class="ic" style="background:#4caf6a"></div><span class="url">huddlemeet.app</span>
      <h5>Huddle Meet</h5><p>Record and transcribe live conversations using the notes bot on every call.</p>
      <div class="foot">Manage<span class="toggle on"></span></div>
    </div>
    <div class="intcard" style="left:466px;top:98px">
      <div class="ic" style="background:#6a6fd1"></div><span class="url">huddlemeet.app</span>
      <h5>Crewroom</h5><p>Use the notes bot to record and generate automatic transcripts of every meeting.</p>
      <div class="foot">Manage<span class="toggle"></span></div>
    </div>
    <div class="intcard" style="left:728px;top:98px">
      <div class="ic" style="background:#3b8ef0"></div><span class="url">huddlemeet.app</span>
      <h5>Vidlane</h5><p>Connect so that meetings are recorded and transcribed automatically when scheduled.</p>
      <div class="foot">Manage<span class="toggle on"></span></div>
    </div>
    <div class="intcard" style="left:204px;top:260px">
      <div class="ic" style="background:#5aa7e8"></div><span class="url">huddlemeet.app</span><h5>Cloudbin Drive</h5>
    </div>
    <div class="intcard" style="left:466px;top:260px">
      <div class="ic" style="background:#f2c94c"></div><span class="url">huddlemeet.app</span><h5>Dayplan Calendar</h5>
    </div>
    <div class="intcard" style="left:728px;top:260px">
      <div class="ic" style="background:#3d7dd8"></div><span class="url">huddlemeet.app</span><h5>Mailport</h5>
    </div>
    <div class="abs fade"></div>
  </div>
</section>

<section class="why">
  <h2 class="abs section-title" style="top:102px">Why Companies Choose BrimLoop</h2>
  <div class="feat dark" style="left:85px;top:208px;height:192px">
    <div class="icon"><b></b></div>
    <h3>Policy-as-Code Simplicity</h3>
    <p>Define rules once. Enforce everywhere — across cloud, on-prem, or hybrid environments.</p>
  </div>
  <div class="feat" style="left:436px;top:208px;height:192px">
    <div class="icon"><b></b></div>
    <h3>AI-Aware Authorization</h3>
    <p>Manage access for human and machine identities alike, including AI agents operating within enterprise systems.</p>
  </div>
  <div class="feat" style="left:787px;top:208px;height:192px">
    <div class="icon"><b></b></div>
    <h3>Zero Trust, Fully Realized</h3>
    <p>Aligns perfectly with modern Zero Trust principles — continuous verification, least privilege, and compliant data handling.</p>
  </div>
  <div class="feat" style="left:85px;top:428px;height:171px">
    <div class="icon"><b></b></div>
    <h3>Developer First</h3>
    <p>DKs, REST APIs, and CLI tools for embedding enforcement right into your CI/CD pipelines.</p>
  </div>
  <div class="feat" style="left:436px;top:428px;height:171px">
    <div class="icon"><b></b></div>
    <h3>Audit &amp; Compliance Ready</h3>
    <p>Every decision logged, replayable, and provable — simplifying compliance checks.</p>
  </div>
</section>

<section class="built">
  <h2 class="abs section-title" style="top:66px">Built for Modern Infrastructure</h2>

  <div class="panel" style="left:99px;top:172px;width:490px;height:407px">
    <div class="login-back" style="left:128px;top:70px;width:236px;height:180px"></div>
    <div class="login">
      <div class="brand"><span class="dot"></span>BrimLoop</div>
      <h6>Welcome!</h6>
      <div class="sm">Sign in to your account</div>
      <div class="sso"><span>Sign in with SSO</span><span>Sign in with key</span></div>
      <div class="sm" style="margin-top:6px">or continue</div>
      <div class="field">Email<div></div></div>
      <div class="field">Password<div></div></div>
      <div class="row"><span>Remember me</span><em>Forgot Password?</em></div>
      <div class="go">Sign in</div>
      <div class="sm" style="margin-top:6px">Don't have an account? Sign up</div>
    </div>
    <div class="abs" style="left:22px;top:322px;width:440px">
      <h3>Unified Policy Engine</h3>
      <p class="desc">Fine-grained authorization that works across applications, APIs, and AI models.</p>
    </div>
  </div>

  <div class="panel" style="left:611px;top:172px;width:490px;height:407px">
    <svg class="abs" style="left:0;top:0" width="490" height="300">
      <path d="M242 92 V128 H120 V152 M242 128 H364 V199" stroke="#d6d8dc" stroke-width="1.2" fill="none"/>
    </svg>
    <div class="flow hot" style="left:182px;top:60px">Fraud Prevention</div>
    <div class="flow" style="left:34px;top:152px;width:174px;height:73px"><h6>badActor</h6><p>Blocked Aug 14th at 14:40</p></div>
    <div class="flow" style="left:273px;top:199px;width:183px;height:71px"><h6>badActor</h6><p>Blocked Aug 14th at 11:40</p></div>
    <div class="abs" style="left:22px;top:322px;width:450px">
      <h3>Real-Time Decisions</h3>
      <p class="desc">Low-latency evaluation powered by in-memory computation, inspired by the best of Dunmere Charter design.</p>
    </div>
  </div>

  <div class="panel" style="left:99px;top:603px;width:1002px;height:289px">
    <div class="abs" style="left:22px;top:28px;width:460px">
      <h3>Enterprise Integrations</h3>
      <p class="desc">Plug into your identity providers (Kestra ID, Korvan, Cobalt Directory) and existing observability tools (Watchhound, Logsift).</p>
    </div>
    <div class="abs" role="img" aria-label="Soft grid backdrop behind integration partner marks" style="left:560px;top:30px;width:400px;height:200px;background:radial-gradient(ellipse at center,#f3f4f6 0%,#ffffff 70%)"></div>
    <svg class="abs" style="left:600px;top:80px" width="320" height="110" role="img" aria-label="Integration partner marks">
      <circle cx="48" cy="32" r="12" fill="#fff" stroke="#c7cbd1" stroke-width="2"/>
      <circle cx="105" cy="32" r="12" fill="#fff" stroke="#5c6270" stroke-width="2"/>
      <line x1="162" y1="52" x2="162" y2="88" stroke="#c7cbd1" stroke-width="1.5"/>
      <line x1="146" y1="88" x2="178" y2="88" stroke="#c7cbd1" stroke-width="1.5"/>
      <circle cx="162" cy="32" r="20" fill="#fff" stroke="#3f6fd8" stroke-width="2.5"/>
      <circle cx="220" cy="32" r="12" fill="#fff" stroke="#7a6fe0" stroke-width="2"/>
      <circle cx="277" cy="32" r="12" fill="#fff" stroke="#2b2f36" stroke-width="2"/>
    </svg>
    <span class="learn" style="left:22px;top:236px">Learn More →</span>
  </div>
</section>

<section class="voices">
  <h2 class="abs section-title" style="top:82px">What Our Customers Say</h2>
  <div class="quote" style="left:140px;top:207px">
    <h3>“With BrimLoop, we finally have one source of truth for data access.”</h3>
    <p>Before implementing BrimLoop, our access policies were fragmented across &nbsp;different teams and systems. Engineers often had to manually approve &nbsp;requests or rewrite rules for each service.</p>
    <p style="margin-top:14px">Now, BrimLoop automatically enforces our access policies across APIs, data pipelines, &nbsp;and AI integrations. Every request is evaluated by the same logic, no &nbsp;exceptions or shadow rules. It’s given both our developers and auditors &nbsp;complete confidence that data access is consistent, compliant, and traceable.</p>
    <div class="who">Jonah Sellers</div>
    <div class="role">CTO, FinTech company</div>
  </div>
  <div class="quote" style="left:634px;top:207px">
    <h3>“Our AI workflows are safe-by-design now, not retrofitted for security.”</h3>
    <p>When we introduced AI into our customer analytics, it quickly became clear &nbsp;that traditional access tools couldn’t handle machine identities. &nbsp;GateMarrow solved that for us. It applies the same least-privilege &nbsp;enforcement to AI agents as it does to people — ensuring bots can’t see &nbsp;or generate sensitive data unless explicitly allowed.</p>
    <p style="margin-top:14px">The best part is that updates to our security policies automatically &nbsp;propagate everywhere — across services, languages, and even models. It’s made our platform’s security completely adaptive without slowing down &nbsp;innovation.</p>
    <div class="who">Reid Sanford</div>
    <div class="role">Head of Engineering, SaaS firm</div>
  </div>
  <div class="abs dots"><span class="on"></span><span></span><span></span></div>
  <div class="abs logo-row" style="left:116px;top:764px;width:970px">
    <span class="logo-item" style="opacity:.6"><span class="mk"></span>Tarsel</span>
    <span class="logo-item"><span class="mk"></span>Harlow</span>
    <span class="logo-item"><span class="mk"></span>Tablewise</span>
    <span class="logo-item"><span class="mk"></span>Chatterbox</span>
    <span class="logo-item"><span class="mk"></span>Tunefold</span>
    <span class="logo-item" style="opacity:.6"><span class="mk"></span>Postwren</span>
  </div>
</section>

<section class="cta-wrap">
  <div class="abs cta">
    <h2>Scale Security at Your Pace</h2>
    <p>Flexible tiers for startups, enterprises, and regulated industries.<br>Pay for what you protect — not per user.</p>
    <span class="go">Get Started</span>
  </div>
</section>

<footer class="site-foot">
  <div class="abs rule"></div>
  <div class="abs brand" style="left:100px;top:70px"><span class="dot"></span>BrimLoop</div>
  <p class="abs" style="left:100px;top:104px;font-size:12.5px;color:var(--text)">2025 BrimLoop. All rights reserved.</p>
  <p class="abs" style="left:100px;top:222px;font-size:12px;color:var(--text)">Follow us on:</p>
  <div class="abs social" style="left:100px;top:250px" aria-label="Social profiles"><span><i></i></span><span><i></i></span><span><i></i></span></div>

  <div class="fcol" style="left:506px"><h5>Product</h5><a>Features</a><a>How it Works</a><a>API &amp; SDK</a><a>Integrations</a><a>Demo</a></div>
  <div class="fcol" style="left:700px"><h5>Resources</h5><a>Documentation</a><a>Tutorials &amp; Guides</a><a>Use Cases</a><a>Blog</a><a>Security &amp; Compliance</a><a>FAQ</a></div>
  <div class="fcol" style="left:902px"><h5>Company</h5><a>About Us</a><a>Careers</a><a>Partners</a><a>Press &amp; News</a><a>Contact</a></div>

  <div class="legal"><a style="left:467px">Privacy Policy</a><a style="left:598px">Security</a><a style="left:695px">Terms</a></div>
</footer>

</body>
</html>
```